Verpackungsdesign für Zigarre
Zielgruppe
KALUN isteine Unternehmung im Baunebenbereich welche sich auf Kabelschächte und Schachtabdeckungen aus Chromstahl spezialisiert hat. Unsere Kunden sind Ingenieure, Planer, Netzbetreiber aus Telecom, Verkehr, Elektro und Industrie. Absatzpartner/Mittler sind auch grössere Bauunternehmungen. Die Ansprechpartner sind meist männlich zwischen 40 und 60 Jahre alt. Wir möchten unseren ausgewählten Kunden neben einer guten Flasche Rum welche wir schon separat gelabelt haben auch eine eigene Zigarre als Geschenk überreichen, da der Inhaber mit manchen Kunden die Leidenschaft Zigarren und Rum teilt. Dazu haben wir vorab1000 Zigarren in der Dominikanischen Republik nach den eigenen Vorgaben herstellen lassen welche, wir jetzt noch mit Banderole ausstatten möchten. Wir suchen ein schönes Design der Banderole (Bauchbinde) und auch eine kreative Verpackung für Gebinde von mehreren Zigarren (z.B. ein Einmachglas mit Etikette anstatt der Holzkistchen welche leider immer nach Gebrauch weggeschmissen werden)
Aufgabenstellung
Die Marke KALUN muss auf der Banderole als Sponsor (oder Überreicher) vermittelt werden. Für die Zigarre selbst haben wir den Namen vonerika ausgewählt. Da dies die erste eigene Zigarre wird soll der Beinamen Edition Eins verwendet werden. Evt. kann auch mit 2 Bauchbinden gearbeitet werden (KALUN und von erika und Edition Typ Eins separat... oder so...Wir benötigen ein Design und Format welches auch kurzfristig recht preisgünstig produziert werden kann. Erwartet wird ein Vorschlag bei welchem die Produktionsmöglichkeit abgeklärt wird (1000 - 5000 Stk. als Erstserie inkl. Druckofferte) Vielleicht bringt auch jemand einen ganz neuen kreativen schönen Vorschlag der Beschriftung...? Wir sind nicht auf Standardpapier eingeschossen - es muss einfach schön, kostengünstig und vorallem einprägsam sein. Bei Erfolg der Aktion überlegen wir uns noch weitere Formate und Zigarren herzustellen und vielleicht auch zu verkaufen anstatt zu verschen unter dem Namen von erika. Für die Verpackung von ganzen Gebinden (10-20 Stk. / Gebinde) suchen wir noch eine kreative Lösung welche sich von den klassischen Holzkistchen unterscheidet. Wir würden uns als Zusatz wünschen, dass der Designer auch dazu Vorschläge mit Beschriftung bringt. Die Farben von KALUN sind rot, chrom und schwarz... (siehe Website www.kalun-beispiel.com) von erika stelel ich mir in Gold vor. Evt. können die Firmenfarben von KALUN untergeordnet vertreten sein um dann komplett nur noch auf den Namen von erika später ohne KALUN mit Nachfolgeprodukten aufzusetzen um diese auch zu verkaufen.

```html
<!DOCTYPE html>
<html lang="de">
<head>
<meta charset="utf-8">
<title>von Erika – Banderole Versionen 3.1 und 3.2</title>
<link rel="stylesheet" href="https://fonts.googleapis.com/css2?family=Arimo&family=Montserrat:ital,wght@1,500;1,700&family=Pinyon+Script&display=swap">
<style>
  :root {
    --paper: #ffffff;
    --ink: #111111;
    --band-black: #232323;
    --band-black-light: #3a3a3a;
    --gold: #e2b84f;
    --gold-light: #f3d27a;
    --gold-deep: #c7962e;
    --leaf: #c99a62;
    --leaf-light: #d7b07c;
  }
  html, body {
    margin: 0;
    padding: 0;
    width: 1200px;
    height: 571px;
    overflow: hidden;
    background: var(--paper);
  }
  .presentation { display: block; width: 1200px; height: 571px; }
  .version-label {
    font-family: "Arimo", Arial, sans-serif;
    font-size: 25px;
    letter-spacing: 1px;
    fill: var(--ink);
  }
  .wordmark {
    font-family: "Pinyon Script", cursive;
    fill: var(--gold);
  }
  .band-caption {
    font-family: "Montserrat", sans-serif;
    font-style: italic;
  }
  .band-caption--dark { font-weight: 700; fill: var(--ink); font-size: 15px; }
  .band-caption--gold { font-weight: 500; fill: var(--gold); font-size: 16px; }
</style>
</head>
<body>
<svg class="presentation" viewBox="0 0 1200 571" xmlns="http://www.w3.org/2000/svg">
  <defs>
    <linearGradient id="leafTone" x1="0" y1="0" x2="1" y2="0">
      <stop offset="0" stop-color="var(--leaf)"/>
      <stop offset="0.5" stop-color="var(--leaf-light)"/>
      <stop offset="1" stop-color="var(--leaf)"/>
    </linearGradient>
    <linearGradient id="goldTone" x1="0" y1="0" x2="1" y2="0">
      <stop offset="0" stop-color="var(--gold-deep)"/>
      <stop offset="0.5" stop-color="var(--gold-light)"/>
      <stop offset="1" stop-color="var(--gold)"/>
    </linearGradient>
    <radialGradient id="slateTone" cx="0.5" cy="0.4" r="0.8">
      <stop offset="0" stop-color="var(--band-black-light)"/>
      <stop offset="1" stop-color="var(--band-black)"/>
    </radialGradient>
    <clipPath id="medallionInner">
      <ellipse cx="880" cy="401" rx="53" ry="88"/>
    </clipPath>
  </defs>

  <!-- Version 3.1 -->
  <g class="version version--one">
    <text class="version-label" transform="translate(119 218) rotate(-90)">VERSION 3.1</text>
    <path class="cigar" role="img" aria-label="Foto einer Zigarre"
          d="M232 571 V100 Q232 62 272 60 H360 Q400 62 400 100 V571 Z" fill="url(#leafTone)"/>

    <g class="band band--classic">
      <rect class="band-edge" x="99" y="324" width="434" height="6" fill="url(#goldTone)"/>
      <rect class="band-field" x="99" y="330" width="434" height="116" fill="url(#slateTone)"/>
      <rect class="band-footer" x="99" y="446" width="434" height="28" fill="url(#goldTone)"/>
      <text class="wordmark" x="310" y="411" font-size="80" text-anchor="middle">von Erika</text>
      <text class="band-caption band-caption--dark" x="162" y="466">FROM KALUN®</text>
      <text class="band-caption band-caption--dark" x="361" y="466">EDITION EINS</text>
      <circle class="seal-ring" cx="316" cy="460" r="38" fill="var(--gold-deep)"/>
      <circle class="seal-core" cx="316" cy="460" r="31" fill="var(--gold)"
              role="img" aria-label="Illustration eines Segelschiffs"/>
    </g>
  </g>

  <!-- Version 3.2 -->
  <g class="version version--two">
    <text class="version-label" transform="translate(683 218) rotate(-90)">VERSION 3.2</text>
    <path class="cigar" role="img" aria-label="Foto einer Zigarre"
          d="M795 571 V100 Q795 62 835 60 H922 Q962 62 962 100 V571 Z" fill="url(#leafTone)"/>

    <g class="band band--medallion">
      <rect class="band-field" x="663" y="342" width="434" height="117" fill="url(#slateTone)"/>
      <rect class="band-rule" x="663" y="353" width="434" height="2" fill="var(--gold)"/>
      <rect class="band-rule" x="663" y="447" width="434" height="2" fill="var(--gold)"/>
      <text class="band-caption band-caption--gold" x="693" y="407">FROM KALUN®</text>
      <text class="band-caption band-caption--gold" x="957" y="407">EDITION EINS</text>

      <ellipse class="medallion" cx="880" cy="401" rx="61" ry="96" fill="url(#slateTone)"/>
      <ellipse class="medallion-frame" cx="880" cy="401" rx="55" ry="90" fill="none"
               stroke="var(--gold)" stroke-width="1.6"/>
      <ellipse class="medallion-emblem" cx="880" cy="343" rx="16" ry="13" fill="var(--gold)"
               role="img" aria-label="Illustration eines Segelschiffs"/>
      <g clip-path="url(#medallionInner)">
        <text class="wordmark" x="880" y="426" font-size="34" text-anchor="middle"
              textLength="118" lengthAdjust="spacingAndGlyphs"
              transform="rotate(-62 880 416)">von Erika</text>
      </g>
    </g>
  </g>
</svg>
</body>
</html>
```